Adult Banner for Escort and Party Girl Website

I would like a banner to use for a campaign on plumby reach and vantra net. Static and GIF. Most fit site size requirements for strip banner.

Our website is lumovel.example.au to give you an idea of what we do.
We provide escorts and party girls for clients in Sydney Australia

Have attached a basic example ideally it should stand out more and be more engaging

Target Market(s)

Men with cash willing to spend on having a companion join them for a fun party

Industry/Entity Type

Adult entertainment

Requirements
Must have
• Must be suitable for posting on plumby reach vantranet sites. Need static and gif designs.
Nice to have
• Be creative and sexy.

```html
<!DOCTYPE html>
<html lang="en">
<head>
<meta charset="utf-8">
<title>Party Strip Banners</title>
<link href="https://fonts.googleapis.com/css2?family=Poppins:ital,wght@0,600;0,700;1,500;1,600&display=swap" rel="stylesheet">
<style>
  :root {
    --page: #ffffff;
    --gold: #c9a03f;
    --gold-soft: #d8b457;
    --white: #ffffff;
    --charcoal: #2b2b2b;
    --charcoal-deep: #141414;
    --cocoa: #3a2522;
    --cocoa-deep: #2a1a18;
    --night: #1d1b20;
    --night-deep: #121114;
  }
  * { margin: 0; padding: 0; box-sizing: border-box; }
  html, body { width: 1200px; height: 494px; overflow: hidden; background: var(--page); }
  body { position: relative; font-family: "Poppins", sans-serif; color: var(--white); }

  .banner { position: absolute; left: 49px; width: 1102px; height: 126px; overflow: hidden; }
  .banner--mono { top: 34px; background: linear-gradient(90deg, var(--charcoal-deep), var(--charcoal) 40%, #1e1e1e); }
  .banner--split { top: 182px; background: linear-gradient(90deg, var(--cocoa-deep), var(--cocoa)); }
  .banner--night { top: 330px; background: linear-gradient(90deg, var(--night-deep), var(--night)); }

  .photo { position: absolute; }
  .banner--mono .photo { left: 713px; top: 0; width: 389px; height: 126px;
    background: linear-gradient(90deg, #2b2b2b, #5a5a5a 30%, #8d8d8d 55%, #3c3c3c 85%, #262626); }
  .banner--split .photo { left: 0; top: 0; width: 1102px; height: 126px;
    clip-path: polygon(318px 0, 836px 0, 800px 126px, 298px 126px);
    background: linear-gradient(100deg, #2e201d 30%, #6b5148 48%, #4a3631 60%, #2a1e1c 80%); }
  .banner--night .photo { left: 0; top: 0; width: 460px; height: 126px;
    background: linear-gradient(90deg, #3a2a24, #6a4d3e 45%, #2c2220 80%, var(--night)); }

  .stripe { position: absolute; inset: 0; background: var(--gold); }
  .stripe--left { clip-path: polygon(307px 0, 323px 0, 302px 126px, 286px 126px); }
  .stripe--right { clip-path: polygon(830px 0, 848px 0, 812px 126px, 794px 126px); }

  .brand { position: absolute; display: flex; align-items: center; justify-content: center;
    border-radius: 50%; background: #0f0f0f; border: 2px solid var(--gold); }
  .brand__name { font-weight: 600; font-size: 13px; letter-spacing: 1px; color: var(--gold); }
  .banner--mono .brand { left: 22px; top: 20px; width: 86px; height: 86px; }
  .banner--night .brand { left: 473px; top: 9px; width: 108px; height: 108px; }
  .banner--night .brand__name { font-size: 15px; }

  .copy { position: absolute; }
  .banner--mono .copy { left: 167px; top: 12px; }
  .banner--night .copy { left: 612px; top: 12px; }
  .headline { font-weight: 700; font-size: 28px; line-height: 38px; }
  .subline { font-weight: 700; font-size: 20px; line-height: 30px; }
  .cta { font-weight: 600; font-style: italic; font-size: 18px; line-height: 28px; }
  .cta__link { color: var(--gold-soft); text-decoration: underline; text-underline-offset: 4px; }

  .tag { position: absolute; background: var(--gold); font-weight: 700; white-space: nowrap; }
  .tag--top { left: 18px; top: 20px; height: 39px; padding: 0 10px; font-size: 26px; line-height: 39px; }
  .tag--bottom { left: 105px; top: 68px; height: 39px; padding: 0 8px 0 10px; font-size: 26px; line-height: 39px; }
  .tag--right { left: 824px; top: 20px; height: 34px; padding: 0 10px; font-size: 20px; line-height: 34px; }
  .banner--split .cta { position: absolute; left: 830px; top: 62px; font-size: 17px; line-height: 23px; }
</style>
</head>
<body>

  <section class="banner banner--mono">
    <div class="photo" role="img" aria-label="Black and white photo of two masked women holding lollipops"></div>
    <div class="brand"><span class="brand__name">LUMOVEL</span></div>
    <div class="copy">
      <p class="headline">Your Party is One Click Away</p>
      <p class="subline">Lumovel Your Night Away</p>
      <p class="cta"><span class="cta__link">Click now</span> to have you&nbsp; dream girl party for you!</p>
    </div>
  </section>

  <section class="banner banner--split">
    <div class="photo" role="img" aria-label="Photo of a woman in a grey sweater lying on a rug"></div>
    <div class="stripe stripe--left"></div>
    <div class="stripe stripe--right"></div>
    <span class="tag tag--top">Your Party is One</span>
    <span class="tag tag--bottom">Click Away</span>
    <span class="tag tag--right">Lumovel Your Night Away</span>
    <p class="cta"><span class="cta__link">Click now</span> to have you<br>dream girl party for you!</p>
  </section>

  <section class="banner banner--night">
    <div class="photo" role="img" aria-label="Photo of a woman lying back holding a cherry above her lips"></div>
    <div class="brand"><span class="brand__name">LUMOVEL</span></div>
    <div class="copy">
      <p class="headline">Your Party is One Click Away</p>
      <p class="subline">Lumovel Your Night Away</p>
      <p class="cta"><span class="cta__link">Click now</span> to have you&nbsp; dream girl party for you!</p>
    </div>
  </section>

</body>
</html>
```